Corporate Travel Technology Company needs new Business Card design

We need a new business card design to reflect our re-branded company. Our company is called vendaXo (pronounced eureka) and we provide Business Intelligence and mobile travel management solutions for the corporate travel industry. Our multinational customers use our solutions to manage large travel budgets and frequent travellers, as well as to save money and reduce risk. We'd like to see designs that use the blue and green palette as well as our corporate logo (attached below). The design should communicate innovation, insight, forward thinking, contemporary, trusted.

Target Market(s)

Large multinational corporates and Travel Agencies.

Industry/Entity Type

Business

Contact Information for Business Card

Marguerite Tallis
Chief Executive
vendaXo
Phone number - +61 (0)2 8147 3092
Email address - marguerite.tallis@vendaxo.example
Mobile number - +61 (0)455 206 718
www.vendaxo.example

Font styles to use
Other font styles liked:
• Please use font as close to corporate logo as possible

Colors
0255a3
0393ce
00a990
33b8a4
33a6d7
3176b5

Requirements
Must have
• Please include the words;
• Mobile Travel Management
• Accelerating Travel Business Insights
• Use corporate logo - although icon can be stylised if needed

```html
<!DOCTYPE html>
<html lang="en">
<head>
<meta charset="utf-8">
<title>vendaXo business card</title>
<link href="https://fonts.googleapis.com/css2?family=Open+Sans:wght@400;600;700&display=swap" rel="stylesheet">
<style>
  :root {
    --stage: #2b2b2d;
    --blue-deep: #1a98da;
    --blue-bright: #06c2e6;
    --blue-text: #1a9ad6;
    --slate: #2f3f47;
    --ink: #3a4348;
    --paper: #ffffff;
    --paper-shade: #eef0f2;
    --faint-on-blue: rgba(0, 60, 120, 0.08);
    --faint-on-white: rgba(40, 120, 180, 0.08);
  }
  * { box-sizing: border-box; margin: 0; padding: 0; }
  html, body {
    width: 1200px; height: 834px; overflow: hidden;
    background: var(--stage);
    font-family: "Open Sans", Arial, sans-serif;
  }
  .canvas { position: relative; width: 1200px; height: 834px; }
  .card {
    position: absolute; width: 560px; height: 320px; overflow: hidden;
    box-shadow: 0 10px 30px rgba(0,0,0,0.45);
  }
  .card-front {
    left: 60px; top: 70px;
    background: radial-gradient(ellipse at 55% 80%, var(--blue-bright) 0%, var(--blue-deep) 75%);
    color: var(--paper);
  }
  .card-back {
    left: 580px; top: 444px;
    background: linear-gradient(135deg, var(--paper-shade) 0%, var(--paper) 60%);
    color: var(--ink);
  }
  .faint-ring { position: absolute; border-radius: 50%; }
  .card-front .faint-ring {
    width: 360px; height: 360px; left: 40px; top: -60px;
    border: 46px solid var(--faint-on-blue);
  }
  .card-back .faint-ring {
    width: 300px; height: 300px; right: 40px; top: -130px;
    border: 40px solid var(--faint-on-white);
  }
  .brand { position: absolute; display: flex; align-items: center; gap: 12px; font-weight: 600; letter-spacing: 0.5px; white-space: nowrap; }
  .brand-dot { border-radius: 50%; flex: none; }
  .card-front .brand { left: 0; right: 0; top: 112px; justify-content: center; font-size: 58px; }
  .card-front .brand-dot { width: 30px; height: 30px; border: 4px solid var(--paper); }
  .card-front .site {
    position: absolute; left: 0; right: 0; top: 214px; text-align: center;
    font-size: 13px; letter-spacing: 0.3px;
  }
  .card-back .brand { right: 42px; top: 124px; font-size: 48px; color: var(--slate); }
  .card-back .brand-dot { width: 26px; height: 26px; border: 4px solid var(--blue-text); }
  .person { position: absolute; left: 40px; top: 120px; }
  .person-name { font-size: 20px; font-weight: 700; color: var(--slate); white-space: nowrap; }
  .person-role { font-size: 15px; color: var(--blue-text); margin-top: 2px; }
  .contacts { position: absolute; left: 40px; top: 196px; list-style: none; }
  .contacts li { display: flex; align-items: center; gap: 12px; font-size: 13px; height: 22px; white-space: nowrap; }
  .contacts svg { width: 14px; height: 14px; flex: none; }
  .contacts .web { color: var(--blue-text); font-weight: 700; }
</style>
</head>
<body>
<main class="canvas">
  <section class="card card-front" aria-label="Card front">
    <div class="faint-ring"></div>
    <div class="brand"><span class="brand-dot"></span><span>vendaXo</span></div>
    <div class="site">www.vendaxo.example</div>
  </section>

  <section class="card card-back" aria-label="Card back">
    <div class="faint-ring"></div>
    <div class="person">
      <div class="person-name">Marguerite Tallis</div>
      <div class="person-role">Chief Executive</div>
    </div>
    <ul class="contacts">
      <li>
        <svg viewBox="0 0 14 14" fill="none" stroke="#1a9ad6" stroke-width="1.4"><rect x="3.5" y="1" width="7" height="12" rx="1.2"/><line x1="6" y1="11" x2="8" y2="11"/></svg>
        <span>+61 (0)455 206 718</span>
      </li>
      <li>
        <svg viewBox="0 0 14 14" fill="none" stroke="#1a9ad6" stroke-width="1.4"><path d="M1.5 5 Q7 1 12.5 5 L11 6.5 L9 5.5 L5 5.5 L3 6.5 Z"/><rect x="3" y="7.5" width="8" height="5" rx="1"/></svg>
        <span>+61 (0)2 8147 3092</span>
      </li>
      <li>
        <svg viewBox="0 0 14 14" fill="none" stroke="#1a9ad6" stroke-width="1.4"><rect x="1" y="3" width="12" height="8.5"/><path d="M1 3 L7 8 L13 3"/></svg>
        <span>marguerite.tallis@vendaxo.example</span>
      </li>
      <li>
        <svg viewBox="0 0 14 14" fill="none" stroke="#1a9ad6" stroke-width="1.3"><circle cx="7" cy="7" r="5.8"/><ellipse cx="7" cy="7" rx="2.6" ry="5.8"/><line x1="1.2" y1="7" x2="12.8" y2="7"/></svg>
        <span class="web">www.vendaxo.example</span>
      </li>
    </ul>
    <div class="brand"><span class="brand-dot"></span><span>vendaXo</span></div>
  </section>
</main>
</body>
</html>
```